Brookfarrow Osteopathy and dry needling business card

Business card for Brookfarrow Osteopathy and Dry Needling.

Industry/Entity Type

Health

Contact Information for Business Card

I do not have a phone number yet. I also do not have an email address yet. The physical address is: 48 Lower Crane Street Brookfarrow The website is: www.brookfarrowosteosteopathy.example My details are: Dr Martin Pellowe, Osteopath (B.Clin.Sci (Ost) M.Ost BSC ECON (Hons)

Colors
0094D4
00A9DD
6FCCEA
C7EBF8
E9F6FB

Requirements
Must have
• logo on the back
Nice to have
• Maybe a space for me to write an appointment time and date on the card.

```html
<!DOCTYPE html>
<html lang="en">
<head>
<meta charset="utf-8">
<title>Brookfarrow Osteopathy and Dry Needling – Business Card</title>
<link rel="stylesheet" href="https://fonts.googleapis.com/css2?family=Open+Sans:ital,wght@0,400;0,600;0,700;1,700&display=swap">
<style>
  :root {
    --canvas: #eeeeef;
    --card: #1e1e1f;
    --card-deep: #161617;
    --ink-grey: #6b6b6c;
    --ink-soft: #5a5a5b;
    --rule: #4a4a4b;
    --paper: #ffffff;
    --ink-dark: #111111;
    --brand-blue: #0094d4;
    --brand-sky: #00a9dd;
  }
  * { box-sizing: border-box; margin: 0; padding: 0; }
  html, body {
    width: 1199px; height: 1200px; overflow: hidden;
    background: var(--canvas);
    font-family: "Open Sans", Arial, sans-serif;
  }
  .card {
    position: absolute; left: 234px; width: 727px; height: 412px;
    border-radius: 28px; background: var(--card); overflow: hidden;
  }
  .card--front { top: 156px; }
  .card--back { top: 650px; height: 418px; }

  /* Front */
  .brand-seal {
    position: absolute; left: 51px; top: 42px; width: 132px; height: 132px;
    display: flex; align-items: center; justify-content: center;
  }
  .brand-seal__ring {
    position: absolute; inset: 0; border: 2px solid var(--ink-soft); border-radius: 50%;
  }
  .brand-seal__name {
    font-weight: 700; font-size: 16px; color: var(--ink-grey); letter-spacing: .3px;
  }
  .practitioner {
    position: absolute; right: 44px; top: 150px; text-align: right; color: var(--ink-grey);
  }
  .practitioner__name { font-weight: 700; font-style: italic; font-size: 30px; line-height: 1.1; letter-spacing: -.3px; }
  .practitioner__title { font-weight: 700; font-style: italic; font-size: 11px; letter-spacing: -.1px; }
  .divider {
    position: absolute; left: 47px; right: 44px; top: 219px; height: 1px; background: var(--rule);
  }
  .address {
    position: absolute; right: 44px; top: 234px; font-weight: 700; font-size: 14px; color: var(--ink-grey);
  }
  .contacts { position: absolute; left: 47px; top: 234px; list-style: none; }
  .contacts li {
    display: flex; align-items: center; gap: 9px; height: 27px;
    font-weight: 700; font-size: 15px; color: var(--ink-grey);
  }
  .contacts svg { width: 20px; height: 20px; flex: none; }

  /* Back */
  .emboss-field {
    position: absolute; inset: 0;
    background: radial-gradient(circle at 30% 60%, #232324, var(--card-deep) 80%);
  }
  .appointment {
    position: absolute; left: 22px; top: 30px; width: 682px; height: 104px;
    background: var(--paper); border-radius: 19px; padding: 10px 16px;
  }
  .appointment__label { font-weight: 600; font-size: 18px; color: var(--ink-dark); font-family: Arial, "Open Sans", sans-serif; }
  .back-mark {
    position: absolute; left: 466px; top: 226px; width: 220px; height: 126px;
    display: flex; align-items: center; gap: 10px;
  }
  .back-mark__dot { width: 34px; height: 34px; border-radius: 50%; background: var(--brand-sky); flex: none; }
  .back-mark__name { font-weight: 700; font-size: 19px; line-height: 1.15; color: var(--brand-blue); }
</style>
</head>
<body>

<section class="card card--front" aria-label="Business card front">
  <div class="brand-seal">
    <span class="brand-seal__ring"></span>
    <span class="brand-seal__name">Brookfarrow</span>
  </div>

  <div class="practitioner">
    <h1 class="practitioner__name">Dr Martin Pellowe</h1>
    <p class="practitioner__title">Osteopath (B.Clin.Sci (Ost) M.Ost BSC ECON (Hons)</p>
  </div>

  <div class="divider"></div>

  <p class="address">48 Lower Crane Street Brookfarrow</p>

  <ul class="contacts">
    <li>
      <svg viewBox="0 0 20 20" fill="none" stroke="#6b6b6c" stroke-width="1.4"><circle cx="10" cy="10" r="8.5"/><circle cx="10" cy="10" r="5"/><path d="M5 10h10M10 5c-2 3-2 7 0 10M10 5c2 3 2 7 0 10"/></svg>
      www.brookfarrowosteosteopathy.example
    </li>
  </ul>
</section>

<section class="card card--back" aria-label="Business card back">
  <div class="emboss-field" role="img" aria-label="Repeating pattern of embossed practice seals, black on black"></div>

  <div class="appointment">
    <p class="appointment__label">Appointment</p>
  </div>

  <div class="back-mark">
    <span class="back-mark__dot"></span>
    <span class="back-mark__name">Brookfarrow Osteopathy</span>
  </div>
</section>

</body>
</html>
```